Business Card Design

we are Marrowbank Farms & we would like a business card that stands out from the crowd and that we can apply this design to our products as we will be also placing orders for labels and stickers in the future

Industry/Entity Type

Business

Contact Information for Business Card

Packing Shed : 53 617 904
mobile : 0412 583 091
email : marrowbankfarms@kestrelnet.com
address : Copperbark Lane Tarrowin 4571

```html
<!DOCTYPE html>
<html lang="en">
<head>
<meta charset="utf-8">
<title>Marrowbank Farms – Business Card</title>
<link rel="stylesheet" href="https://fonts.googleapis.com/css2?family=Gelasio:wght@400;500&family=Arimo:wght@400&display=swap">
<style>
  :root {
    --backdrop: #ece7df;
    --card: #ffffff;
    --green: #1b4d2b;
    --red: #d42a2f;
    --rule: #1a1a1a;
  }
  * { box-sizing: border-box; margin: 0; padding: 0; }
  html, body { width: 1189px; height: 1200px; overflow: hidden; }
  body { background: var(--backdrop); position: relative; font-family: "Arimo", Arial, sans-serif; }

  .card {
    position: absolute;
    left: 171px;
    width: 855px;
    height: 486px;
    background: var(--card);
    border-radius: 24px;
    border: 1px solid #ddd6ca;
  }
  .card--front { top: 67px; }
  .card--back { top: 626px; }

  .brand {
    position: absolute;
    display: flex;
    align-items: center;
    gap: 14px;
    font-family: "Gelasio", Georgia, serif;
    font-weight: 500;
    color: var(--green);
    white-space: nowrap;
  }
  .brand__dot { border-radius: 50%; background: var(--red); flex: none; }

  .card--front .brand { left: 50%; top: 50%; transform: translate(-50%, -50%); font-size: 46px; }
  .card--front .brand__dot { width: 34px; height: 34px; }

  .card--back .brand { left: 193px; top: 200px; transform: translate(-50%, -50%); font-size: 30px; }
  .card--back .brand__dot { width: 22px; height: 22px; }

  .divider {
    position: absolute;
    left: 381px;
    top: 88px;
    width: 2px;
    height: 312px;
    background: var(--rule);
  }

  .person { position: absolute; left: 419px; top: 105px; }
  .person__name {
    font-family: "Gelasio", Georgia, serif;
    font-weight: 400;
    font-size: 39px;
    line-height: 44px;
    color: var(--green);
    letter-spacing: 0.5px;
  }
  .person__role { font-size: 25px; line-height: 28px; color: var(--red); }

  .shed {
    position: absolute;
    left: 419px;
    top: 232px;
    font-size: 23px;
    color: var(--green);
  }
  .shed__label { color: var(--red); }

  .contacts {
    position: absolute;
    left: 419px;
    top: 283px;
    list-style: none;
  }
  .contacts__item {
    display: flex;
    align-items: center;
    gap: 10px;
    height: 34px;
    font-size: 22px;
    color: var(--green);
  }
  .contacts__icon {
    width: 27px; height: 27px;
    background: var(--red);
    border-radius: 3px;
    flex: none;
  }
</style>
</head>
<body>
  <section class="card card--front">
    <div class="brand"><span class="brand__dot"></span>Marrowbank Farms</div>
  </section>

  <section class="card card--back">
    <div class="brand"><span class="brand__dot"></span>Marrowbank Farms</div>
    <div class="divider"></div>

    <div class="person">
      <p class="person__name">Employee Name</p>
      <p class="person__role">Owner</p>
    </div>

    <p class="shed"><span class="shed__label">Packing Shed :</span> 53 617 904</p>

    <ul class="contacts">
      <li class="contacts__item">
        <svg class="contacts__icon" viewBox="0 0 27 27" aria-hidden="true">
          <rect x="9" y="5" width="9" height="17" rx="1.5" fill="none" stroke="#fff" stroke-width="1.6"/>
          <rect x="11" y="8" width="5" height="5" fill="#fff"/>
          <circle cx="13.5" cy="18.5" r="1.2" fill="#fff"/>
        </svg>
        0412 583 091
      </li>
      <li class="contacts__item">
        <svg class="contacts__icon" viewBox="0 0 27 27" aria-hidden="true">
          <rect x="6" y="8" width="15" height="11" fill="none" stroke="#fff" stroke-width="1.6"/>
          <path d="M6 8 L13.5 14.5 L21 8 M6 19 L11.5 13 M21 19 L15.5 13" fill="none" stroke="#fff" stroke-width="1.4"/>
        </svg>
        marrowbankfarms@kestrelnet.com
      </li>
      <li class="contacts__item">
        <svg class="contacts__icon" viewBox="0 0 27 27" aria-hidden="true">
          <path d="M13.5 5 C9.5 5 7.5 8 7.5 11 C7.5 15 13.5 22 13.5 22 C13.5 22 19.5 15 19.5 11 C19.5 8 17.5 5 13.5 5 Z" fill="none" stroke="#fff" stroke-width="1.6"/>
          <circle cx="13.5" cy="11" r="2.3" fill="#fff"/>
        </svg>
        Copperbark Lane Tarrowin 4571
      </li>
    </ul>
  </section>
</body>
</html>
```